Card for modern wood artisan that builds log homes and timber frames.

Design a card with catchy imagery. With a quick list of things I build and services I offer.

I'd like an English side and a french side. I can provide the text.

I am basically a guy that builds log homes and timber frames , but I am very eco friendly oriented.

I use only eco friendly products to limit my carbon footprint.
I want the client to feel as if they are hiring a good smart builder.

I have been building for a while but just starting out to market myself out there , not just work for other companies. Starting
My own thing legitimately.

I am very conscientious, and I take care of the work I do. I am trying to bring a new age, modern feel to an old profession.

Reason: I am not completely satisfied with A model yet, looking for that masculin rustic artistic design that I havent completely found yet. Thank you for your sumbissions.

Target Market(s)

People looking to hire a builder to design and build their projects.
And contractors that want to hire a quality subcontractor for their jobs.

Industry/Entity Type

Construction

Contact Information for Business Card

I want my logo on it, that I had designed here.
And a list of services I provide.

With my phone number, website adress and Email.

Requirements
Must have
• Artful presentation,
• Eco friendly feel
• I love trees.

```html
<!DOCTYPE html>
<html lang="en">
<head>
<meta charset="utf-8">
<title>Forvane — Business Card</title>
<link rel="stylesheet" href="https://fonts.googleapis.com/css2?family=Montserrat:wght@400;500;600&display=swap">
<style>
  :root {
    --backdrop: #222222;
    --card: #ffffff;
    --gold: #d29a2c;
    --gold-light: #e8bf63;
    --gold-deep: #b98322;
    --ink: #1f1f1f;
    --muted: #3a3a3a;
  }
  * { box-sizing: border-box; margin: 0; padding: 0; }
  html, body {
    width: 1200px;
    height: 930px;
    overflow: hidden;
    background: var(--backdrop);
    font-family: "Montserrat", sans-serif;
  }
  .stage { position: relative; width: 1200px; height: 930px; }

  .card {
    position: absolute;
    width: 680px;
    height: 400px;
    background: var(--card);
    border-radius: 22px;
    box-shadow: 0 14px 30px rgba(0,0,0,0.45);
    overflow: hidden;
  }
  .card--front { left: 80px; top: 45px; }
  .card--back { left: 440px; top: 485px; }

  .artwork {
    position: absolute;
    border-radius: 10px;
    background: linear-gradient(180deg, var(--gold-light) 0%, var(--gold) 55%, var(--gold-deep) 100%);
  }
  .card--front .artwork { left: 270px; top: 48px; width: 140px; height: 200px; }
  .card--back .artwork { right: 80px; top: 40px; width: 96px; height: 138px; }

  .brand {
    position: absolute;
    display: flex;
    align-items: center;
    gap: 12px;
    color: var(--ink);
    font-weight: 600;
    letter-spacing: 3px;
    text-transform: uppercase;
    white-space: nowrap;
  }
  .brand__square { width: 16px; height: 16px; background: var(--gold); }
  .card--front .brand {
    left: 50%;
    top: 300px;
    transform: translate(-50%, -50%);
    font-size: 36px;
  }
  .card--back .brand {
    right: 60px;
    top: 200px;
    font-size: 20px;
    letter-spacing: 2px;
  }
  .card--back .brand__square { width: 11px; height: 11px; }

  .contact { position: absolute; left: 48px; bottom: 40px; }
  .contact__name {
    color: var(--gold);
    font-size: 30px;
    font-weight: 500;
    letter-spacing: 1px;
    text-transform: uppercase;
    line-height: 1;
  }
  .contact__role { color: var(--muted); font-size: 17px; margin-top: 6px; }
  .contact__line {
    margin-top: 14px;
    font-size: 15px;
    color: var(--muted);
    white-space: nowrap;
  }
  .contact__label { color: var(--gold); font-weight: 500; }
  .contact__sep { color: var(--gold); margin: 0 6px; }
</style>
</head>
<body>
  <main class="stage">
    <section class="card card--front" aria-label="Card front">
      <div class="artwork" role="img" aria-label="Hand-sketched golden pine tree with exposed roots"></div>
      <div class="brand">
        <span class="brand__square"></span>
        <span class="brand__name">Forvane</span>
      </div>
    </section>

    <section class="card card--back" aria-label="Card back">
      <div class="artwork" role="img" aria-label="Small hand-sketched golden pine tree with exposed roots"></div>
      <div class="brand">
        <span class="brand__square"></span>
        <span class="brand__name">Forvane</span>
      </div>
      <div class="contact">
        <p class="contact__name">Maren Holt</p>
        <p class="contact__role">President</p>
        <p class="contact__line">
          <span class="contact__label">P :</span> 800-555-0142<span class="contact__sep">|</span><span class="contact__label">E :</span> mholt@forvanemail.com<span class="contact__sep">|</span><span class="contact__label">W :</span> www.forvanebuilds.com
        </p>
      </div>
    </section>
  </main>
</body>
</html>
```